BRAVO Property Concierge

We require a website built for this company. Logo is also on the attached document. Some info on the company:<br/>To create a work class experience for our clients for property maintenance. A personalised service that deliver’s what landlords need...Quality work, on time and managed from start to finish.<br/>We do things different, our clients deal with one contact, a client manager who manages your maintenance task from start to finish. Our service allows our expert trades people to do what they do best and leave the management/organising to us!<br/>I have drafted up the layout of the web ... very brief at this stage however once we have more info we will add links and can collate more information and provide. <br/>We just want to get a layout of what you think the web should look like and can go from there.

```html
<!DOCTYPE html>
<html lang="en">
<head>
<meta charset="utf-8">
<title>BRAVO Property Concierge</title>
<link href="https://fonts.googleapis.com/css2?family=Roboto:wght@300;400;500;700;900&display=swap" rel="stylesheet">
<style>
:root{
  --yellow:#f7c400;
  --gold:#b99a2a;
  --dark:#3d3d3d;
  --ink:#1e1e1e;
  --muted:#a9a9a9;
  --light:#ececec;
  --mid:#dedede;
  --white:#ffffff;
}
*{margin:0;padding:0;box-sizing:border-box}
html,body{width:1200px;height:4081px;overflow:hidden}
body{position:relative;font-family:'Roboto',sans-serif;color:var(--ink);background:var(--white)}
.abs{position:absolute}
/* hero */
.hero{left:0;top:0;width:1200px;height:553px;background:linear-gradient(100deg,#c9a82a 0%,#b99424 45%,#8c7a3a 75%,#c9a830 100%)}
.header-bar{left:0;top:0;width:1200px;height:109px;background:rgba(40,36,28,.72)}
.brand{left:66px;top:14px;color:var(--white)}
.brand-name{font-size:52px;font-weight:700;letter-spacing:-1px;line-height:52px}
.brand-sub{font-size:17px;font-weight:700;line-height:18px}
.nav{top:36px;font-size:18px;font-weight:700;color:var(--white)}
.social-dot{left:1106px;top:37px;width:22px;height:22px;border-radius:50%;background:var(--white)}
.hero-title{left:75px;top:136px;width:520px;font-size:48px;font-weight:900;line-height:57px;color:var(--white)}
.hero-copy{left:75px;top:326px;width:515px;height:131px;background:rgba(60,50,20,.45);color:var(--white);font-size:15.5px;font-weight:700;line-height:25px;padding:8px 10px}
.hero-btn{left:133px;top:487px;width:399px;height:47px;background:var(--yellow);color:var(--white);font-size:18px;font-weight:700;display:flex;align-items:center;justify-content:center;gap:6px}
.video{left:609px;top:185px;width:516px;height:290px;background:#1c1c1c;color:var(--white);overflow:hidden}
.video-title{left:58px;top:20px;font-size:17px}
.video-avatar{left:14px;top:12px;width:34px;height:34px;border-radius:50%;background:#555}
.video-action{top:12px;font-size:12px;font-weight:500;text-align:center}
.video-big{left:0;top:100px;width:516px;text-align:center;font-size:40px;line-height:42px;color:#777;font-weight:300}
/* services */
.section-title{font-size:60px;font-weight:700;color:var(--ink)}
.svc{width:356px;height:199px;text-align:center;padding-top:20px}
.svc h3{font-size:22px;font-weight:500;color:var(--ink)}
.svc .rule{width:40px;height:2px;background:var(--yellow);margin:22px auto 0}
.svc p{font-size:14px;font-weight:300;color:#8a8a8a;line-height:27px;margin:30px auto 0;width:280px}
/* safe */
.safe-title{left:66px;top:1328px;font-size:58px;font-weight:700;line-height:61px}
.yline{height:2px;background:var(--yellow)}
.feat{left:415px;width:680px}
.feat .star{position:absolute;left:0;top:-6px;font-size:20px}
.feat h4{margin-left:26px;font-size:22px;font-weight:500}
.feat p{margin-left:26px;margin-top:6px;font-size:14px;font-weight:300;color:#bdbdbd}
/* banner */
.banner{left:0;top:1702px;width:1200px;height:389px;background:linear-gradient(90deg,#d8d8d8 0%,#ececec 40%,#c8c8c8 80%,#dcdcdc 100%)}
.banner-title{left:0;top:1836px;width:1200px;text-align:center;font-size:41px;font-weight:500}
.outline-btn{left:525px;top:1904px;width:149px;height:46px;border:2px solid #555;font-size:14px;display:flex;align-items:center;justify-content:center;color:#333}
/* about */
.img-block{position:absolute}
.sub-title{font-size:21px;font-weight:500}
.small-copy{font-size:14px;font-weight:300;color:#bbb;line-height:25px;width:290px}
/* team */
.team-band{left:0;top:2832px;width:1200px;height:159px;background:var(--dark)}
.team-col{top:2991px;width:400px;height:371px;text-align:center}
.avatar{width:108px;height:108px;border-radius:50%;margin:42px auto 0}
.team-col h3{font-size:33px;font-weight:700;margin-top:46px;line-height:34px}
.team-col .role{font-size:14px;letter-spacing:5px;color:#777;margin-top:4px}
.team-col p{font-size:14px;font-weight:300;color:#8a8a8a;line-height:27px;width:280px;margin:18px auto 0}
/* visit */
.visit-title{left:158px;top:3455px;font-size:46px;font-weight:700;color:var(--yellow);letter-spacing:-1px}
.contact-row{left:158px;font-size:18px;font-weight:300;color:#333;display:flex;align-items:center;gap:16px}
.contact-row svg{width:14px;height:14px}
.map{left:609px;top:3465px;width:423px;height:282px;background:linear-gradient(135deg,#e9e6da,#f2e8c4 50%,#dfe8d4)}
/* footer */
.footer{left:0;top:3850px;width:1200px;height:231px;background:var(--dark);border-top:4px solid var(--yellow)}
.fcol{top:3920px;color:var(--white)}
.fcol h5{font-size:16px;font-weight:500;margin-bottom:12px}
.fcol a{display:flex;align-items:center;gap:8px;font-size:13px;color:#ddd;text-decoration:none;line-height:24px}
.fcol a i{width:10px;height:10px;border-radius:50%;background:#ddd;display:inline-block}
.email{left:809px;top:3922px;width:307px;height:43px;background:var(--white);color:#999;font-size:14px;padding:12px 15px}
.subscribe{left:809px;top:3976px;width:307px;height:43px;background:var(--yellow);color:var(--white);font-size:14px;font-weight:700;display:flex;align-items:center;justify-content:center}
</style>
</head>
<body>

<!-- Hero -->
<div class="abs hero" role="img" aria-label="Photo of a person relaxing by a window overlooking a city, tinted yellow"></div>
<div class="abs header-bar"></div>
<div class="abs brand">
  <div class="brand-name">BRAVO</div>
  <div class="brand-sub">Property Concierge</div>
</div>
<div class="abs nav" style="left:751px">Home</div>
<div class="abs nav" style="left:842px">Services</div>
<div class="abs nav" style="left:955px">Contact</div>
<div class="abs social-dot"></div>

<h1 class="abs hero-title">Manage all your maintenance needs in one place</h1>
<p class="abs hero-copy">We do things different, our clients deal with one contact, a client manager who manages your maintenance task from start to finish. Our service allows our expert trades people to do what they do best and leave the management/organising to us!</p>
<div class="abs hero-btn">HAVE A LOOK AT OUR SERVICES
  <svg width="18" height="18" viewBox="0 0 18 18"><circle cx="9" cy="9" r="7.5" fill="none" stroke="#fff" stroke-width="1.8"/><path d="M9 4.5v8M5.5 9.5L9 13l3.5-3.5" fill="none" stroke="#fff" stroke-width="1.8"/></svg>
</div>

<div class="abs video" role="img" aria-label="Embedded video placeholder">
  <div class="abs video-avatar"></div>
  <div class="abs video-title">video placeholder</div>
  <div class="abs video-action" style="left:375px">
    <svg width="18" height="18" viewBox="0 0 18 18"><circle cx="9" cy="9" r="8" fill="#fff"/><path d="M9 4v5l3 2" stroke="#1c1c1c" stroke-width="1.6" fill="none"/></svg><br>Watch later</div>
  <div class="abs video-action" style="left:460px">
    <svg width="18" height="18" viewBox="0 0 18 18"><path d="M10 3l7 6-7 6v-4C5 11 2 13 1 16c0-6 4-9 9-9z" fill="#fff"/></svg><br>Share</div>
  <svg class="abs" style="left:138px;top:40px" width="240" height="240" viewBox="0 0 240 240"><circle cx="120" cy="120" r="110" fill="none" stroke="#2e2e2e" stroke-width="16"/></svg>
  <div class="video-big abs">VIDEO<br>PLACEHOLDER</div>
  <svg class="abs" style="left:249px;top:136px" width="18" height="20" viewBox="0 0 18 20"><path d="M2 1l15 9-15 9z" fill="#fff"/></svg>
</div>

<!-- Services -->
<h2 class="abs section-title" style="left:0;top:622px;width:1200px;text-align:center">Our services</h2>
<div class="abs svc" style="left:66px;top:762px;background:#ebebeb"><h3>Wealth Creation</h3><div class="rule"></div><p>Lorem ipsum dolor sit amet, consectetur adipiscing elit.</p></div>
<div class="abs svc" style="left:422px;top:762px;background:#dfdfdf"><h3>Finance</h3><div class="rule"></div><p>Lorem ipsum dolor sit amet, consectetur adipiscing elit.</p></div>
<div class="abs svc" style="left:778px;top:762px;background:#ebebeb"><h3>Tradespeople</h3><div class="rule"></div><p>Lorem ipsum dolor sit amet, consectetur adipiscing elit.</p></div>
<div class="abs svc" style="left:66px;top:961px;background:#dcdcdc"><h3>Removalist van and trailers</h3><div class="rule"></div><p>Lorem ipsum dolor sit amet, consectetur adipiscing elit.</p></div>
<div class="abs svc" style="left:422px;top:961px;background:#ebebeb"><h3>Smoke Alarms</h3><div class="rule"></div><p>Lorem ipsum dolor sit amet, consectetur adipiscing elit.</p></div>
<div class="abs svc" style="left:778px;top:961px;background:#dcdcdc"><h3>Connections</h3><div class="rule"></div><p>Lorem ipsum dolor sit amet, consectetur adipiscing elit.</p></div>

<!-- Safe time and money -->
<h2 class="abs safe-title">Safe<br>time<br>and<br>money</h2>
<div class="abs yline" style="left:66px;top:1594px;width:52px"></div>
<div class="abs feat" style="top:1308px"><span class="star">★</span><h4>Customer service</h4><p>Click edit button to change this text. Lorem ipsum dolor sit amet, consectetur adipiscing elit.</p></div>
<div class="abs feat" style="top:1402px"><span class="star">★</span><h4>Values</h4><p>Click edit button to change this text. Lorem ipsum dolor sit amet, consectetur adipiscing elit.</p></div>
<div class="abs feat" style="top:1497px"><span class="star">★</span><h4>Call Center</h4><p>Click edit button to change this text. Lorem ipsum dolor sit amet, consectetur adipiscing elit.</p></div>
<div class="abs feat" style="top:1591px"><span class="star">★</span><h4>Pricing</h4><p>Click edit button to change this text. Lorem ipsum dolor sit amet, consectetur adipiscing elit.</p></div>

<!-- Banner -->
<div class="abs banner" role="img" aria-label="Faded photo of a man sitting by a window above a city skyline"></div>
<h2 class="abs banner-title">Find out all the ways we benefit our customers</h2>
<div class="abs outline-btn">CONTACT US</div>

<!-- About -->
<h2 class="abs section-title" style="left:66px;top:2178px;font-size:58px">Our about</h2>
<div class="abs yline" style="left:66px;top:2266px;width:52px"></div>
<div class="img-block" style="left:454px;top:2217px;width:291px;height:339px;background:linear-gradient(90deg,#2a2a2a,#9a9a9a 55%,#cfcfcf)" role="img" aria-label="Black and white photo of people walking past a modern building"></div>
<h3 class="abs sub-title" style="left:454px;top:2574px">Our values</h3>
<p class="abs small-copy" style="left:454px;top:2611px">Lorem ipsum dolor sit amet, consectetur adipiscing elit. Ut elit tellus, luctus nec ullamcorper mattis, pulvinar dapibus leo.</p>
<h3 class="abs sub-title" style="left:810px;top:2289px">Our mission</h3>
<p class="abs small-copy" style="left:810px;top:2326px">Lorem ipsum dolor sit amet, consectetur adipiscing elit. Ut elit tellus, luctus nec ullamcorper mattis, pulvinar dapibus leo.</p>
<div class="img-block" style="left:810px;top:2440px;width:291px;height:192px;background:linear-gradient(160deg,#6f8fc0,#c9d6e6 45%,#2c3e5c)" role="img" aria-label="Photo of a glass office tower against a cloudy sky"></div>

<!-- Team -->
<div class="abs team-band"></div>
<h2 class="abs" style="left:0;top:2880px;width:1200px;text-align:center;font-size:48px;font-weight:700;color:#fff">Meet the team</h2>
<div class="abs team-col" style="left:0;background:#f5f5f5">
  <div class="avatar" style="background:#b07a66" role="img" aria-label="Portrait of team member Maren"></div>
  <h3>Maren</h3><div class="role">JOB DESCRIPTION</div>
  <p>Lorem ipsum dolor sit amet, consectetur adipiscing elit.</p>
</div>
<div class="abs team-col" style="left:400px;background:#f5f5f5">
  <div class="avatar" style="background:#5a4840" role="img" aria-label="Portrait of team member Tobias"></div>
  <h3>Tobias</h3><div class="role">JOB DESCRIPTION</div>
  <p>Lorem ipsum dolor sit amet, consectetur adipiscing elit.</p>
</div>
<div class="abs team-col" style="left:800px;background:#ebebeb">
  <div class="avatar" style="background:#8a7a70" role="img" aria-label="Portrait of team member Owen"></div>
  <h3>Owen</h3><div class="role">JOB DESCRIPTION</div>
  <p>Lorem ipsum dolor sit amet, consectetur adipiscing elit.</p>
</div>

<!-- Visit -->
<h2 class="abs visit-title">VISIT US</h2>
<div class="abs yline" style="left:160px;top:3535px;width:52px;background:#e6e6e6"></div>
<div class="abs contact-row" style="top:3576px"><svg viewBox="0 0 14 14"><path d="M7 1a4 4 0 0 1 4 4c0 3-4 8-4 8S3 8 3 5a4 4 0 0 1 4-4z" fill="#aaa"/><circle cx="7" cy="5" r="1.5" fill="#fff"/></svg>1450 Harbor Ave. Fairview, CA 90412</div>
<div class="abs contact-row" style="top:3623px"><svg viewBox="0 0 14 14"><rect x="1" y="3" width="12" height="9" fill="#aaa"/><path d="M1 3l6 5 6-5" stroke="#fff" fill="none"/></svg>hello@bravoconcierge.example</div>
<div class="abs contact-row" style="top:3670px"><svg viewBox="0 0 14 14"><rect x="2" y="1" width="10" height="12" rx="1" fill="#aaa"/><rect x="4" y="3" width="6" height="6" fill="#fff"/></svg>(555) 210 44 16</div>
<div class="abs contact-row" style="top:3717px"><svg viewBox="0 0 14 14"><rect x="1" y="4" width="12" height="9" fill="#aaa"/><rect x="3" y="1" width="8" height="4" fill="#aaa"/><rect x="3" y="7" width="8" height="2" fill="#fff"/></svg>(555) 210 44 33</div>
<div class="abs map" role="img" aria-label="Street map showing the office location"></div>

<!-- Footer -->
<div class="abs footer"></div>
<div class="abs fcol" style="left:84px"><h5>Get Started</h5><a href="#">Resources</a><a href="#">Tutorials</a><a href="#">Examples</a><a href="#">Docs</a></div>
<div class="abs fcol" style="left:241px"><h5>About</h5><a href="#">Stories</a><a href="#">Community</a><a href="#">Blog</a><a href="#">Brand Assets</a></div>
<div class="abs fcol" style="left:399px"><h5>Features</h5><a href="#">Overview</a><a href="#">Design</a><a href="#">Code</a><a href="#">Collaborate</a></div>
<div class="abs fcol" style="left:556px"><h5>Follow Us</h5><a href="#"><i></i>Friendbook</a><a href="#"><i></i>Chirper</a><a href="#"><i></i>VidStream</a><a href="#"><i></i>Snapgram</a></div>
<div class="abs email">Email</div>
<div class="abs subscribe">SUBSCRIBE</div>

</body>
</html>
```